Need Amazing Website for Consulting Company

We need an amazing website design for a Human Resources Consulting Company. This will be geared towards a more professional crowd, but we don't want it to be overly corporate and stuffy: Just, clean and professional and amazing. Please use the video link below for further instruction.

http://clipvesta.net/v/kqPzRmN4

Thank You.

PS Logo file has been attached.

Target Market(s)

The target marketing is small business owners who have employees. These owners cant afford an in-house HR person so they would hire this client to consult and do the work for them.

Industry/Entity Type

It Company

Font styles to use
Sans Serif

Requirements
Must have
• Please watch video:

Must have spot for video on homepage.
Nice to have
• Clean, professional, but not overly corporate, we want a personal and fun feel to this site a bit to separate them from all the other executive type sites. This site should have some LIFE to it and reflect a local brand that is doing great things.
Should not have
• Should not be just a corporate site, should not be overly stuffy, should not be overly boring.

```html
<!DOCTYPE html>
<html lang="en">
<head>
<meta charset="utf-8">
<title>Mesa Ridge HR Consulting</title>
<link href="https://fonts.googleapis.com/css2?family=Lato:wght@300;400;700;900&display=swap" rel="stylesheet">
<style>
:root{
  --red:#c0212f;
  --ink:#222;
  --card:#2a2a2a;
  --panel:rgba(30,30,32,.82);
  --grey-band:#e3e3e3;
  --white:#fff;
}
*{margin:0;padding:0;box-sizing:border-box}
html,body{width:1154px;height:1200px;overflow:hidden;background:#fff;font-family:'Lato',Arial,sans-serif;color:var(--ink)}
.page{position:relative;width:1154px;height:1200px}
.abs{position:absolute}

/* header */
.brand{left:204px;top:12px;display:flex;align-items:center;gap:8px}
.brand-name{font-weight:900;font-size:20px;line-height:1.05;color:#111;letter-spacing:.5px}
.brand-name small{display:block;font-weight:400;font-size:11px;letter-spacing:0;color:#333}
.brand-mark{width:26px;height:26px;background:var(--red)}

.nav{left:0;top:89px;width:1154px;height:38px;background:var(--red);display:flex;justify-content:center;align-items:center;gap:11px}
.nav a{color:var(--white);text-decoration:none;font-weight:700;font-size:11px;letter-spacing:1px;white-space:nowrap}
.nav span{color:#f3c3c7;font-size:11px}

/* hero */
.hero{left:0;top:127px;width:1154px;height:285px;background:linear-gradient(180deg,#5f8fc9 0%,#9fbde0 35%,#b9794c 62%,#8a5a35 100%)}
.video{left:204px;top:142px;width:452px;height:255px;background:linear-gradient(120deg,#e8eef4 0%,#cdd9e6 45%,#f4f4f2 100%);overflow:hidden}
.video-tagline{left:265px;top:18px;color:var(--red);font-weight:300;font-size:20px;line-height:1.2}
.video-play{left:163px;top:95px}
.controls{left:18px;top:212px;width:416px;height:31px;display:flex;align-items:center;gap:6px}
.controls .btn{width:50px;height:31px;background:#3a3d40;border-radius:3px;display:flex;align-items:center;justify-content:center}
.controls .bar{flex:1;height:26px;background:#3a3d40;border-radius:3px;display:flex;align-items:center;padding:0 8px;gap:8px}
.track{flex:1;height:7px;background:#1d1f21;position:relative}
.track i{position:absolute;left:0;top:0;height:7px;width:30%;background:#2f9be0}
.hd{color:#2f9be0;font-weight:900;font-size:11px;font-style:normal}

.intro{left:668px;top:142px;width:280px;height:255px;background:var(--panel);padding:0 17px;color:var(--white)}
.intro h2{font-size:10.5px;font-weight:700;letter-spacing:1px;text-align:center;white-space:nowrap;padding:12px 0 10px;border-bottom:1px solid #666}
.intro-photo{margin-top:13px;height:84px;background:linear-gradient(90deg,#e9e2da,#c9d2dc)}
.intro p{font-size:10px;line-height:1.32;margin-top:8px;text-align:justify}
.qualities{position:absolute;left:17px;right:17px;bottom:10px;border-top:1px solid #666;padding-top:8px;display:flex;justify-content:space-between;font-size:12px;font-weight:300;letter-spacing:.3px}
.qualities b{font-weight:300;color:#aaa}

/* cards */
.card{top:460px;width:177px;height:308px;background:var(--card)}
.card-tab{position:absolute;left:0;top:0;width:155px;height:34px;background:var(--red);color:var(--white);font-weight:700;font-size:10.5px;letter-spacing:.9px;white-space:nowrap;padding:12px 0 0 11px}
.card-img{position:absolute;left:10px;top:45px;width:160px;height:151px}
.card-text{position:absolute;left:9px;top:208px;width:160px;color:var(--white);font-size:10px;line-height:1.3;text-align:justify}
.card-list{position:absolute;left:9px;top:208px;width:160px;color:var(--white);font-size:9.5px;line-height:1}
.card-list li{list-style:none;margin-bottom:12px;white-space:nowrap}
.more{position:absolute;right:0;bottom:0;width:64px;height:22px;background:#151515;color:var(--red);font-size:7px;font-weight:900;letter-spacing:.6px;text-align:center;padding-top:8px}

/* testimonials and clients */
.band{left:0;top:787px;width:1154px;height:173px;background:var(--grey-band)}
.quote{left:204px;top:812px;width:410px;height:119px;background:#f1f1f1;border:1px solid #d2d2d2;box-shadow:0 2px 3px rgba(0,0,0,.15)}
.quote-photo{position:absolute;left:14px;top:23px;width:80px;height:80px;background:linear-gradient(160deg,#d9d4cc,#8e8780)}
.quote p{position:absolute;left:103px;top:21px;width:292px;font-size:10px;line-height:1.3;color:#555;text-align:justify}
.quote-meta{position:absolute;right:14px;bottom:10px;font-size:9.5px;color:#444}
.quote-meta b{margin-right:8px}
.clients-title{left:668px;top:812px;width:232px;text-align:center;font-size:11px;letter-spacing:1.5px;color:#333}
.client-frame{left:668px;top:848px;width:232px;height:78px;background:#d0d0d0;padding:9px}
.client-logo{width:100%;height:100%;background:var(--white);display:flex;align-items:center;justify-content:center;font-weight:900;font-size:14px;color:#111;letter-spacing:.5px}
.arrow{top:874px}

/* footer */
.stripe{left:0;top:978px;width:1154px;height:18px;background:repeating-linear-gradient(45deg,#cfcfcf 0 2px,#e9e9e9 2px 4px)}
.footer{left:0;top:996px;width:1154px;height:168px;background:linear-gradient(90deg,#3a3430 0%,#2c302b 50%,#3b3f3a 100%)}
.col h3{font-size:11px;font-weight:700;letter-spacing:1.3px;color:var(--white);margin-bottom:15px}
.links li{list-style:none;font-size:10px;color:var(--white);height:23px;border-bottom:1px solid rgba(255,255,255,.12);width:200px;padding-top:1px}
.contact li{list-style:none;font-size:10.5px;color:var(--white);display:flex;gap:10px;height:23px;align-items:flex-start}
.contact li.cont{height:19px;padding-left:22px}
.contact svg{flex:none;margin-top:1px}
.social{display:flex;gap:9px}
.social span{width:26px;height:26px;background:var(--white);border-radius:4px;display:flex;align-items:center;justify-content:center;font-size:7px;font-weight:700;color:#222}
.copyright{left:0;top:1164px;width:1154px;height:36px;background:var(--red);color:var(--white);font-size:10.5px;text-align:center;padding-top:12px}
</style>
</head>
<body>
<div class="page">

  <header>
    <div class="abs brand">
      <div class="brand-name">MESA RIDGE HR<small>Consulting, LLC.</small></div>
      <div class="brand-mark"></div>
    </div>
    <nav class="abs nav">
      <a href="#">HOME</a><span>/</span>
      <a href="#">ETHOS</a><span>/</span>
      <a href="#">SERVICES</a><span>/</span>
      <a href="#">NEWS &amp; MEDIA</a><span>/</span>
      <a href="#">CLIENTELE</a><span>/</span>
      <a href="#">OUR UNIQUE OFFERINGS</a><span>/</span>
      <a href="#">HR SOLUTIONS</a>
    </nav>
  </header>

  <section class="abs hero" role="img" aria-label="Desert landscape with a roadside welcome sign under a blue sky"></section>

  <div class="abs video">
    <div class="abs" style="left:0;top:0;width:452px;height:255px" role="img" aria-label="Relaxed businessman leaning back at his desk"></div>
    <div class="abs video-tagline">Relaxed!,<br>While we do the job</div>
    <svg class="abs video-play" width="66" height="66" viewBox="0 0 66 66"><circle cx="33" cy="33" r="31" fill="none" stroke="#c0212f" stroke-width="2.5"/><path d="M26 20 L47 33 L26 46 Z" fill="none" stroke="#c0212f" stroke-width="2.5" stroke-linejoin="round"/></svg>
    <div class="abs controls">
      <div class="btn"><svg width="12" height="13"><path d="M0 0 L12 6.5 L0 13Z" fill="#fff"/></svg></div>
      <div class="bar">
        <div class="track"><i></i></div>
        <svg width="26" height="10"><g fill="#2f9be0"><rect x="0" y="0" width="2" height="10"/><rect x="4" y="0" width="2" height="10"/><rect x="8" y="0" width="2" height="10"/><rect x="12" y="0" width="2" height="10"/><rect x="16" y="0" width="2" height="10"/><rect x="20" y="0" width="2" height="10"/></g></svg>
        <em class="hd">HD</em>
        <svg width="10" height="10"><path d="M0 0h4M0 0v4M10 0h-4M10 0v4M0 10h4M0 10v-4M10 10h-4M10 10v-4" stroke="#fff" stroke-width="2"/></svg>
      </div>
    </div>
  </div>

  <aside class="abs intro">
    <h2>WE ARE A DIFFERENT KINF OF AGENCY</h2>
    <div class="intro-photo" role="img" aria-label="Smiling consultant with colleagues in an office"></div>
    <p>Mesa Ridge HR Consulting, LLC. (MRHRC) is an experienced consulting agency that is committed to providing businesses with effective and efficient Human Resources support by developing partner-ships to meet company's individual needs.</p>
    <div class="qualities"><span>EFFECTIVE</span><b>&#10022;</b><span>EXPERIENCED</span><b>&#10022;</b><span>EFFICIENT</span></div>
  </aside>

  <article class="abs card" style="left:204px">
    <div class="card-tab">SERVICE AREAS</div>
    <div class="card-img" style="background:linear-gradient(135deg,#4a4f57,#8b9099)" role="img" aria-label="Suit and tie with a wrench in the pocket"></div>
    <p class="card-text">Maecenas eu placerat ante. Fusce ut neque justo, et aliquet enim. In hac habitasse platea dictumst. Nullam commodo neque erat, vitae facilisis erat.</p>
    <div class="more">LEARN MORE</div>
  </article>

  <article class="abs card" style="left:392px">
    <div class="card-tab">THOUGHT LEADERSHIP</div>
    <div class="card-img" style="background:linear-gradient(135deg,#e7e9ec,#b7c0ca)" role="img" aria-label="Businesswoman drawing on a glass board"></div>
    <p class="card-text">Maecenas eu placerat ante. Fusce ut neque justo, et aliquet enim. In hac habitasse platea dictumst. Nullam commodo neque erat, vitae facilisis erat.</p>
    <div class="more">LEARN MORE</div>
  </article>

  <article class="abs card" style="left:583px">
    <div class="card-tab">HR SOLUTIONS</div>
    <div class="card-img" style="background:linear-gradient(180deg,#5d95cf,#cfe1ef 60%,#7aa2b8)" role="img" aria-label="Hand holding a puzzle piece against the sky"></div>
    <ul class="card-list"><li>HR solution for the PUBLIC SECTOR</li><li>HR solution for the CORPORATE</li><li>ROLE BASED HR solution for the</li></ul>
    <div class="more">LEARN MORE</div>
  </article>

  <article class="abs card" style="left:773px">
    <div class="card-tab">NEWS &amp; MEDIA</div>
    <div class="card-img" style="background:linear-gradient(135deg,#c9c3bb,#7f8a73)" role="img" aria-label="Person with a laptop surrounded by newspapers"></div>
    <p class="card-text">Maecenas eu placerat ante. Fusce ut neque justo, et aliquet enim. In hac habitasse platea dictumst. Nullam commodo neque erat, vitae facilisis erat.</p>
    <div class="more">LEARN MORE</div>
  </article>

  <section class="abs band"></section>
  <blockquote class="abs quote">
    <div class="quote-photo" role="img" aria-label="Portrait of the client giving the testimonial"></div>
    <p>Maecenas eu placerat ante. Fusce ut neque justo, et aliquet enim. In hac habitasse platea dictumst. Nullam commodo neque erat, vitae facilisis erat.Maecenas eu placerat ante. Fusce ut neque justo, et aliquet enim. In hac habitasse platea dictumst. Nullam commodo neque erat, vitae facilisis erat.</p>
    <div class="quote-meta"><b>Sam Hollis /</b> 14 Mar 2050 @ 11:07am</div>
  </blockquote>

  <h2 class="abs clients-title">OUR SUCCESSFUL CLIENTS</h2>
  <div class="abs client-frame"><div class="client-logo">BRIGHTLINE STUDIOS</div></div>
  <svg class="abs arrow" style="left:634px" width="28" height="28" viewBox="0 0 28 28"><circle cx="14" cy="14" r="13" fill="#fff"/><path d="M16 8 L10 14 L16 20" fill="none" stroke="#bbb" stroke-width="2.5"/></svg>
  <svg class="abs arrow" style="left:910px" width="28" height="28" viewBox="0 0 28 28"><circle cx="14" cy="14" r="13" fill="#fff"/><path d="M12 8 L18 14 L12 20" fill="none" stroke="#bbb" stroke-width="2.5"/></svg>

  <div class="abs stripe"></div>
  <footer class="abs footer" role="img" aria-label="Desert highway at dusk"></footer>

  <div class="abs col" style="left:222px;top:1020px">
    <h3>ABOUT US</h3>
    <ul class="links"><li>Frequently Asked Questions</li><li>HR Services</li><li>Carrer with us</li><li>Why Choose Us</li><li>Our Company</li></ul>
  </div>

  <div class="abs col" style="left:480px;top:1020px">
    <h3>CONTACT US</h3>
    <ul class="contact">
      <li><svg width="12" height="9" viewBox="0 0 12 9"><rect width="12" height="9" fill="#fff"/><path d="M0 0 L6 5 L12 0" fill="none" stroke="#2b2d2a" stroke-width="1.2"/></svg>info@mesaridgehr.com</li>
      <li><svg width="12" height="12" viewBox="0 0 12 12"><path d="M2 0 L4.5 3 L3.2 4.5 C4 6.5 5.5 8 7.5 8.8 L9 7.5 L12 10 L10.5 12 C5 11.5 0.5 7 0 1.5 Z" fill="#fff"/></svg>(505) 555-0142</li>
      <li style="height:19px"><svg width="12" height="13" viewBox="0 0 12 13"><path d="M6 0 C2.7 0 1 2.3 1 4.7 C1 8 6 13 6 13 C6 13 11 8 11 4.7 C11 2.3 9.3 0 6 0Z" fill="#fff"/><circle cx="6" cy="4.8" r="1.8" fill="#2b2d2a"/></svg>MRHRC, LLC.</li>
      <li class="cont">P.O. Box 40210</li>
      <li class="cont">Riverbend, NM 87000</li>
    </ul>
  </div>

  <div class="abs col" style="left:787px;top:1020px">
    <h3>GET SOCIAL</h3>
    <div class="social"><span>Chirp</span><span>Circle</span><span>Linkr</span><span><svg width="14" height="10" viewBox="0 0 14 10"><rect width="14" height="10" fill="#222"/><path d="M0 0 L7 6 L14 0" fill="none" stroke="#fff" stroke-width="1.3"/></svg></span></div>
  </div>

  <div class="abs copyright">Mesa Ridge HR Consulting, LLC, All rights reserved</div>
</div>
</body>
</html>
```